General Dental Office Business Card

I run a private general dental office in southern California, and would like a refresh/redesign of my business card. I focus on quality care rather than volume. The email address on the uploaded current card should be updated to: info@ferncrestvaledental.com. The current card's logo is a deboss, but I am open to other ideas. The logo can be refreshed, but it is something that's been with me since the beginning of the office, so I wouldn't want a drastic redesign.
Target Market(s)
Adults 18-99, whoever needs dental services
Industry/Entity Type
Healthcare/Dental
Contact Information for Business Card
Name, Address, Phone, email
Colors
Designer to choose colors to be used in the design.
Requirements
Must have
- Logo (Same as original one in the uploaded file), space on back for appointment time/date

```html
<!DOCTYPE html>
<html lang="en">
<head>
<meta charset="utf-8">
<title>Ferncrest Vale Dental – Business Card</title>
<link rel="stylesheet" href="https://fonts.googleapis.com/css2?family=Lato:ital,wght@0,400;0,700;0,900;1,400&display=swap">
<style>
  :root {
    --stage: #1d1d1f;
    --paper: #ffffff;
    --teal: #2fb3bf;
    --navy-light: #1d5f84;
    --navy-dark: #123f5c;
    --ink-light: #ffffff;
    --ink-grey: #444a50;
    --dots: #6b7278;
    --emboss: #5fb4e4;
  }
  * { box-sizing: border-box; margin: 0; padding: 0; }
  html, body { width: 1200px; height: 875px; overflow: hidden; }
  body {
    background: var(--stage);
    font-family: "Lato", sans-serif;
    display: flex;
    align-items: center;
    justify-content: center;
    gap: 40px;
  }
  .card {
    width: 540px;
    height: 310px;
    border-radius: 20px;
    position: relative;
    overflow: hidden;
  }

  /* Appointment side */
  .card--appointment { background: var(--paper); padding: 34px 38px; }
  .brand { display: flex; align-items: center; gap: 18px; justify-content: center; }
  .brand__mark {
    width: 78px; height: 78px; border-radius: 50%;
    border: 3px solid var(--teal);
  }
  .brand__name {
    color: var(--teal);
    font-weight: 400;
    font-size: 34px;
    line-height: 1.05;
    letter-spacing: 1px;
    text-transform: uppercase;
  }
  .fields { margin-top: 38px; display: flex; flex-direction: column; gap: 18px; }
  .field-row { display: flex; align-items: baseline; gap: 6px; }
  .field__label {
    color: var(--teal); font-size: 14px; letter-spacing: 0.5px; text-transform: uppercase;
  }
  .field__line {
    flex: 1; border-bottom: 1.5px dotted var(--dots); transform: translateY(-3px);
  }
  .field__suffix { color: var(--teal); font-size: 12px; }
  .notice {
    margin-top: 22px; text-align: center;
    font-style: italic; font-size: 12px; line-height: 1.45; color: var(--ink-grey);
  }

  /* Contact side */
  .card--contact {
    background: radial-gradient(circle at 75% 40%, var(--navy-light) 0%, var(--navy-dark) 80%);
    padding: 40px 38px;
  }
  .emboss-circle {
    position: absolute; right: 30px; top: 26px;
    width: 196px; height: 196px; border-radius: 50%;
    border: 6px solid var(--emboss);
    opacity: 0.75;
  }
  .contact__content { position: relative; z-index: 1; width: 270px; }
  .contact__brand {
    color: var(--teal); font-size: 32px; line-height: 1.05;
    letter-spacing: 1px; text-transform: uppercase; font-weight: 400;
  }
  .contact__person { margin-top: 16px; }
  .contact__name {
    color: var(--ink-light); font-weight: 900; font-size: 21px; letter-spacing: 0.3px;
    text-transform: uppercase; white-space: nowrap;
  }
  .contact__role { color: var(--teal); font-size: 15px; margin-top: 2px; }
  .contact__list { list-style: none; margin-top: 16px; display: flex; flex-direction: column; gap: 5px; }
  .contact__item {
    display: flex; align-items: flex-start; gap: 10px;
    color: var(--ink-light); font-size: 14px; line-height: 1.3; white-space: nowrap;
  }
  .contact__icon { width: 13px; height: 13px; flex: none; margin-top: 3px; fill: var(--teal); }
</style>
</head>
<body>

  <section class="card card--appointment" aria-label="Appointment card">
    <div class="brand">
      <span class="brand__mark"></span>
      <div class="brand__name">Ferncrest<br>Vale Dental</div>
    </div>
    <div class="fields">
      <div class="field-row">
        <span class="field__label">Name</span><span class="field__line"></span>
      </div>
      <div class="field-row">
        <span class="field__label">Date</span><span class="field__line"></span>
        <span class="field__label">Time</span><span class="field__line"></span>
        <span class="field__suffix">AM\PM</span>
      </div>
    </div>
    <p class="notice">If you are unable to keep your appointment, please call us to<br>reschedule at least 48 hours prior to your appointment.</p>
  </section>

  <section class="card card--contact" aria-label="Contact card">
    <span class="emboss-circle"></span>
    <div class="contact__content">
      <div class="contact__brand">Ferncrest<br>Vale Dental</div>
      <div class="contact__person">
        <div class="contact__name">Marcus T. Ellery DDS</div>
        <div class="contact__role">General Dentistry</div>
      </div>
      <ul class="contact__list">
        <li class="contact__item">
          <svg class="contact__icon" viewBox="0 0 24 24"><path d="M12 2a7 7 0 0 0-7 7c0 5 7 13 7 13s7-8 7-13a7 7 0 0 0-7-7zm0 9.5A2.5 2.5 0 1 1 12 6.5a2.5 2.5 0 0 1 0 5z"/></svg>
          <span>2180 Alder Creek Road<br>Ferncrest, CA 926</span>
        </li>
        <li class="contact__item">
          <svg class="contact__icon" viewBox="0 0 24 24"><path d="M6.6 10.8a15 15 0 0 0 6.6 6.6l2.2-2.2a1 1 0 0 1 1-.25 11.4 11.4 0 0 0 3.6.57 1 1 0 0 1 1 1V20a1 1 0 0 1-1 1A17 17 0 0 1 3 4a1 1 0 0 1 1-1h3.5a1 1 0 0 1 1 1c0 1.25.2 2.45.57 3.6a1 1 0 0 1-.25 1z"/></svg>
          <span>555-014-2290</span>
        </li>
        <li class="contact__item">
          <svg class="contact__icon" viewBox="0 0 24 24"><path d="M2 5h20v14H2zm2 2v.5l8 5 8-5V7l-8 5z"/></svg>
          <span>info@ferncrestvaledental.com</span>
        </li>
        <li class="contact__item">
          <svg class="contact__icon" viewBox="0 0 24 24"><circle cx="12" cy="12" r="10"/></svg>
          <span>ferncrestvaledental.com</span>
        </li>
      </ul>
    </div>
  </section>

</body>
</html>
```